Business Card for Used Machinery Dealer
Brelton-Sakowitz, Evan Tolliver
Business Card for Used Machinery Dealer - Manufacturing
Creative Brief
Use standard fonts
Designer may use whatever fonts they see fit
Professional
Warren Tolliver
President
7819 E. 142nd St. Maple Hollow IL 60917
warrentollivrxq@mailnest-example.com
www.breltonsakowitz-example.com
Feel free to think out of the box. The color of the card stock may be white, or may be something else. We are open to using glossy or matted. The card stock should probably be a little thick to give it some extra presence. Try different fonts. Maybe the same as the logo would be good maybe something different
If the designer has a great idea for the back of a card I am open to looking at it. Likely the back of the card would consist of our email address. www.breltonsakowitz-example.com

```html
<!DOCTYPE html>
<html lang="en">
<head>
<meta charset="utf-8">
<title>Brelton-Sakowitz Stationery</title>
<link href="https://fonts.googleapis.com/css2?family=Roboto:wght@400;700;900&display=swap" rel="stylesheet">
<style>
  :root {
    --brand-blue: #1f58b5;
    --blue-light: #3d8ee0;
    --blue-dark: #1a3b8c;
    --orange-light: #f8a81c;
    --orange-dark: #ee5b24;
    --paper: #ffffff;
    --stage: #ffffff;
    --frame: #e6e6e6;
    --ink-grey: #777777;
  }
  * { box-sizing: border-box; margin: 0; padding: 0; }
  html, body { width: 1200px; height: 681px; overflow: hidden; background: var(--stage); }
  body { font-family: "Roboto", Arial, sans-serif; position: relative; }
  .stage-frame {
    position: absolute; left: 18px; top: 18px; width: 1164px; height: 636px;
    border: 1px solid var(--frame);
  }
  .sheet {
    position: absolute; background: var(--paper);
    box-shadow: 2px 3px 6px rgba(0,0,0,0.35);
  }
  .brand { position: absolute; display: flex; align-items: center; gap: 6px; }
  .brand-dot { border-radius: 50%; background: var(--brand-blue); flex: none; }
  .brand-name { color: var(--brand-blue); font-weight: 900; letter-spacing: 0.2px; white-space: nowrap; }
  .tagline { position: absolute; color: var(--ink-grey); font-size: 4px; letter-spacing: 0.6px; font-weight: 700; white-space: nowrap; }
  .band-blue {
    position: absolute; left: 0; right: 0;
    background: linear-gradient(90deg, var(--blue-light), var(--blue-dark));
    color: #fff; display: flex; align-items: center; white-space: nowrap;
  }
  .band-orange {
    position: absolute; left: 0; right: 0;
    background: linear-gradient(90deg, var(--orange-light), var(--orange-dark));
    color: #fff; display: flex; flex-direction: column; justify-content: center; white-space: nowrap;
  }

  /* envelope front */
  .envelope-front { left: 60px; top: 96px; width: 516px; height: 240px; }
  .envelope-front .brand { left: 34px; top: 24px; }
  .envelope-front .brand-dot { width: 22px; height: 22px; }
  .envelope-front .brand-name { font-size: 13px; }
  .envelope-front .tagline { left: 34px; top: 54px; }
  .envelope-front .band-blue { top: 154px; height: 14px; font-size: 5px; padding-left: 14px; }
  .envelope-front .band-orange { top: 170px; height: 38px; font-size: 5px; padding-left: 14px; gap: 2px; }

  /* envelope back */
  .envelope-back { left: 60px; top: 384px; width: 516px; height: 252px; }
  .envelope-back .flap { position: absolute; left: 0; top: 0; }
  .envelope-back .brand { left: 50%; top: 30px; transform: translateX(-50%); }
  .envelope-back .brand-dot { width: 16px; height: 16px; }
  .envelope-back .brand-name { font-size: 10px; }

  /* letterhead */
  .letterhead { left: 619px; top: 48px; width: 329px; height: 581px; }
  .letterhead .brand { left: 22px; top: 26px; }
  .letterhead .brand-dot { width: 20px; height: 20px; }
  .letterhead .brand-name { font-size: 11px; }
  .letterhead .tagline { left: 22px; top: 52px; font-size: 3.5px; }
  .letterhead .band-blue { top: 509px; height: 12px; font-size: 4px; padding-left: 12px; }
  .letterhead .band-orange { top: 523px; height: 29px; font-size: 4px; padding-left: 12px; gap: 2px; }

  /* business card */
  .card-front { left: 967px; top: 120px; width: 173px; height: 115px; }
  .card-front .brand { left: 10px; top: 12px; gap: 4px; }
  .card-front .brand-dot { width: 12px; height: 12px; }
  .card-front .brand-name { font-size: 7px; }
  .card-front .tagline { left: 10px; top: 29px; font-size: 2.5px; letter-spacing: 0.3px; }
  .card-front .person { position: absolute; left: 10px; top: 40px; font-size: 4px; color: var(--brand-blue); font-weight: 700; line-height: 1.3; }
  .card-front .person span { display: block; font-weight: 400; color: var(--ink-grey); }
  .card-front .band-blue { top: 72px; height: 8px; font-size: 2.8px; padding-left: 8px; }
  .card-front .band-orange { top: 82px; height: 22px; font-size: 2.8px; padding-left: 8px; gap: 1px; }

  .card-back { left: 967px; top: 254px; width: 173px; height: 106px; }
  .card-back .brand { left: 50%; top: 50%; transform: translate(-50%, -50%); gap: 4px; }
  .card-back .brand-dot { width: 12px; height: 12px; }
  .card-back .brand-name { font-size: 7px; }
</style>
</head>
<body>
  <div class="stage-frame"></div>

  <section class="sheet envelope-front">
    <div class="brand"><span class="brand-dot"></span><span class="brand-name">BRELTON-SAKOWITZ</span></div>
    <div class="tagline">USED MACHINERY • PARTS • SERVICE</div>
    <div class="band-blue">7819 E. 142nd St. • Maple Hollow IL 60917</div>
    <div class="band-orange">
      <span>Phone: (708) 555-0142 • Cell: (708) 555-0187 • Fax: (708) 555-0163</span>
      <span>Email: warrentollivrxq@mailnest-example.com • www.breltonsakowitz-example.com</span>
    </div>
  </section>

  <section class="sheet envelope-back">
    <svg class="flap" width="516" height="252" viewBox="0 0 516 252" aria-hidden="true">
      <path d="M2 2 Q20 50 42 56 L474 56 Q496 50 514 2" fill="none" stroke="#9a9a9a" stroke-width="1"/>
    </svg>
    <div class="brand"><span class="brand-dot"></span><span class="brand-name">BRELTON-SAKOWITZ</span></div>
  </section>

  <section class="sheet letterhead">
    <div class="brand"><span class="brand-dot"></span><span class="brand-name">BRELTON-SAKOWITZ</span></div>
    <div class="tagline">USED MACHINERY • PARTS • SERVICE</div>
    <div class="band-blue">7819 E. 142nd St. • Maple Hollow IL 60917</div>
    <div class="band-orange">
      <span>Phone: (708) 555-0142 • Cell: (708) 555-0187 • Fax: (708) 555-0163</span>
      <span>Email: warrentollivrxq@mailnest-example.com • www.breltonsakowitz-example.com</span>
    </div>
  </section>

  <section class="sheet card-front">
    <div class="brand"><span class="brand-dot"></span><span class="brand-name">BRELTON-SAKOWITZ</span></div>
    <div class="tagline">USED MACHINERY • PARTS • SERVICE</div>
    <div class="person">Warren Tolliver<span>President</span></div>
    <div class="band-blue">7819 E. 142nd St. • Maple Hollow IL 60917</div>
    <div class="band-orange">
      <span>Phone: (708) 555-0142 • Cell: (708) 555-0187</span>
      <span>warrentollivrxq@mailnest-example.com</span>
      <span>www.breltonsakowitz-example.com</span>
    </div>
  </section>

  <section class="sheet card-back">
    <div class="brand"><span class="brand-dot"></span><span class="brand-name">BRELTON-SAKOWITZ</span></div>
  </section>
</body>
</html>
```